Talbek vodka

With the logo attached in the subsequent file, a business card that reflects a premium and organic vodka. On the first side, the company logo in large. The names must be included on the back of the card (Mateo Ignacio Dalmau Ferrerons with the number +34 655 219 870 and Oriol Batlle Quintana and +34 677 341 592). The slogan "What binds us" and "Organic and permium vodka" in bold E-mail (talbekvodka@mailora.net); Website www.talbekvodkaorg.net

```html
<!DOCTYPE html>
<html lang="en">
<head>
<meta charset="utf-8">
<title>Talbek Vodka – Business Card</title>
<link rel="stylesheet" href="https://fonts.googleapis.com/css2?family=Cinzel:wght@400&family=Montserrat:wght@300;400&display=swap">
<style>
  :root {
    --backdrop: #e6e4e1;
    --card: #333436;
    --name: #dcdcdc;
    --contact: #a3a3a3;
    --mark: #9a9b9d;
    --tagline: #b8b8b8;
  }
  * { margin: 0; padding: 0; box-sizing: border-box; }
  html, body { width: 1200px; height: 1000px; overflow: hidden; }
  body { background: var(--backdrop); position: relative; }

  .card {
    position: absolute;
    left: 266px;
    width: 666px;
    height: 396px;
    background: var(--card);
  }
  .card--contacts { top: 75px; }
  .card--brand { top: 534px; }

  .contacts { position: absolute; left: 46px; top: 130px; }
  .person__name {
    font-family: "Cinzel", serif;
    font-size: 21px;
    line-height: 28px;
    color: var(--name);
    letter-spacing: 0.3px;
  }
  .person__phone, .contacts__line {
    font-family: "Montserrat", sans-serif;
    font-weight: 300;
    font-size: 16px;
    color: var(--contact);
    letter-spacing: 0.4px;
  }
  .person__phone { margin-top: 2px; line-height: 22px; }
  .person + .person { margin-top: 14px; }
  .contacts__web { margin-top: 16px; }
  .contacts__line { line-height: 26px; }

  .brand-name {
    position: absolute;
    left: 0; right: 0;
    top: 196px;
    text-align: center;
    font-family: "Montserrat", sans-serif;
    font-weight: 400;
    font-size: 46px;
    line-height: 56px;
    color: var(--mark);
    letter-spacing: 1px;
  }

  .tagline {
    position: absolute;
    left: 0; right: 0;
    top: 346px;
    text-align: center;
    font-family: "Montserrat", sans-serif;
    font-weight: 400;
    font-size: 16px;
    color: var(--tagline);
    letter-spacing: 0.3px;
  }
</style>
</head>
<body>
  <section class="card card--contacts">
    <div class="contacts">
      <div class="person">
        <p class="person__name">Dalmau Ferrerons<br>Mateo Ignacio</p>
        <p class="person__phone">+34 655 219 870</p>
      </div>
      <div class="person">
        <p class="person__name">Oriol Batlle Quintana</p>
        <p class="person__phone">+34 677 341 592</p>
      </div>
      <div class="contacts__web">
        <p class="contacts__line">talbekvodka@mailora.net</p>
        <p class="contacts__line">www.talbekvodkaorg.net</p>
      </div>
    </div>
  </section>

  <section class="card card--brand">
    <p class="brand-name">Talbek vodka</p>
    <p class="tagline">Organic and Permium vodka</p>
  </section>
</body>
</html>
```